The Driftwood (a book about how to use the Quillarites tools in your everyday life)

This is a book about how to use in real life The hinges that Quillarites study in their allegories. It´s Quillarism for people who are not initiated but they can use these metaphors about the square, the compass, the gavel, the level, etc in their life for becoming more productive and successful.

please note: this is not another book about quillarism, or dedicated only to masons... it´s for mothers, workers, bus drivers, CEOs, students and professors. Everybody can take advantage in their lives of using this tools.

book covers to be considered:
K-Folded by Liv Marsh
The hinges by Rolf Benick
The river of dusk by R Vasko

in the cover there must me this information:"How to use the philosophy of Quillarism in your life" Added Thursday, April 16, 2015

Target Market(s)

people who read Delmir, Marco Fedrini, Irve.
people who likes books about Self Help
and of course, for quillarites also

Font styles to use
Serif

Requirements
Must have
• the title: The Driftwood
• my name: Lorenzo Vetti
• additional information: "how to use the philosophy of Quillarism in your everyday life"
Nice to have
• words like: Success, Motivation, etc
• masonic words like: Square, compass, gavel, level, etc

```html
<!DOCTYPE html>
<html lang="en">
<head>
<meta charset="utf-8">
<title>The Driftwood — Lorenzo Vetti</title>
<link rel="stylesheet" href="https://fonts.googleapis.com/css2?family=Bebas+Neue&family=Open+Sans:wght@400;500&display=swap">
<style>
  :root {
    --charcoal: #3a393c;
    --lime: #d3ef00;
    --ink: #3a393c;
  }
  * { margin: 0; padding: 0; box-sizing: border-box; }
  html, body { width: 848px; height: 1200px; overflow: hidden; background: var(--charcoal); }
  .cover {
    position: relative;
    width: 848px;
    height: 1200px;
    background: var(--charcoal);
    overflow: hidden;
  }
  .author-band {
    position: absolute;
    left: 0; top: 88px;
    width: 848px; height: 171px;
    background: var(--lime);
    display: flex; align-items: center; justify-content: center;
  }
  .author-name {
    font-family: "Bebas Neue", "Arial Narrow", sans-serif;
    font-size: 54px;
    letter-spacing: 0.22em;
    color: var(--ink);
    padding-left: 0.22em;
  }
  .title-frame {
    position: absolute;
    left: 85px; top: 445px;
    width: 678px; height: 339px;
  }
  .title-frame svg { display: block; }
  .title {
    position: absolute;
    left: 0; top: 0;
    width: 848px;
    font-family: "Open Sans", "Helvetica Neue", sans-serif;
    font-weight: 500;
    color: var(--lime);
    text-align: center;
    line-height: 1;
  }
  .title-small {
    position: absolute;
    left: 0; width: 848px; top: 522px;
    font-size: 76px;
    letter-spacing: -0.01em;
  }
  .title-large {
    position: absolute;
    left: 0; width: 848px; top: 594px;
    font-size: 112px;
    letter-spacing: -0.03em;
  }
  .tagline-band {
    position: absolute;
    left: 0; top: 950px;
    width: 848px; height: 250px;
    background: var(--lime);
  }
  .tagline {
    position: absolute;
    left: 0; top: 108px;
    width: 848px;
    text-align: center;
    font-family: "Bebas Neue", "Arial Narrow", sans-serif;
    font-size: 25px;
    line-height: 40px;
    letter-spacing: 0.2em;
    color: var(--ink);
  }
</style>
</head>
<body>
<main class="cover">
  <header class="author-band">
    <p class="author-name">Lorenzo Vetti</p>
  </header>

  <div class="title-frame">
    <svg width="678" height="339" viewBox="0 0 678 339" fill="none" stroke="#d3ef00" stroke-width="2">
      <rect x="1" y="1" width="676" height="337"/>
      <rect x="50" y="40" width="572" height="260"/>
      <line x1="1" y1="1" x2="50" y2="40"/>
      <line x1="677" y1="1" x2="622" y2="40"/>
      <line x1="1" y1="338" x2="50" y2="300"/>
      <line x1="677" y1="338" x2="622" y2="300"/>
    </svg>
  </div>

  <h1 class="title">
    <span class="title-small">The</span>
    <span class="title-large">Driftwood</span>
  </h1>

  <footer class="tagline-band">
    <p class="tagline">How to use the philosophy of Quillarism<br>in your everyday life</p>
  </footer>
</main>
</body>
</html>
```